Bold Flyer Needed for Bold Little Gym

We need a 1 page flyer created for our small boutique fitness facility, KorVesta, which highlights a new service we are offering.
We are now offering Red Light Therapy (RLT) to our members and I need a full color, 1 page flyer created that captures the eye of our members while highlighting the benefits and clearly stating the prices at the bottom of the page.
Flyer will be printed out on a standard 8.5" x 11" sheet of paper and should be laid out in a way that is easy to read. Landscape or Portrait layouts are both expectable.
We are using Quorvane Glow Therapy Lights TelaRix 700 Lamps as found here http://lnkzo.example/7QWPL4M
I have attached the text that should be included and our logo for branding of the flyer.
Thank you!

```html
<!DOCTYPE html>
<html lang="en">
<head>
<meta charset="utf-8">
<title>KorVesta – Red Light Therapy Room Flyer</title>
<link href="https://fonts.googleapis.com/css2?family=Bebas+Neue&family=Oswald:wght@500;700&family=Poppins:wght@400;600;700&display=swap" rel="stylesheet">
<style>
  :root{
    --ink:#161616;
    --red:#e3232d;
    --yellow:#f5cc17;
    --white:#ffffff;
    --text-soft:#e6e6e6;
    --stage:#d9d9d9;
  }
  *{box-sizing:border-box;margin:0;padding:0}
  html,body{width:1200px;height:1200px;overflow:hidden;background:var(--stage)}
  .flyer{position:absolute;left:165px;top:37px;width:870px;height:1126px;background:var(--ink);overflow:hidden;font-family:'Poppins',sans-serif;color:var(--white)}
  .hero-photo{position:absolute;left:250px;top:0;width:620px;height:620px;
    background:radial-gradient(ellipse at 85% 20%,#f7a9c6 0%,#d9476f 22%,transparent 48%),
               radial-gradient(ellipse at 45% 40%,#7a3a30 0%,#3b2222 40%,transparent 70%),
               linear-gradient(90deg,var(--ink) 0%,#2a1c1c 30%,#4a2a2a 100%)}
  .hero-fade{position:absolute;left:250px;top:0;width:320px;height:620px;background:linear-gradient(90deg,var(--ink),rgba(22,22,22,0))}
  .hero-fade-bottom{position:absolute;left:0;top:470px;width:870px;height:160px;background:linear-gradient(180deg,rgba(22,22,22,0),var(--ink))}

  .brand{position:absolute;left:52px;top:140px;font-family:'Oswald',sans-serif;font-weight:700;font-size:46px;color:var(--yellow);letter-spacing:1px;line-height:1}
  .headline{position:absolute;left:50px;top:200px;font-family:'Bebas Neue',sans-serif;line-height:.9;font-weight:400}
  .headline .intro{font-size:46px;color:var(--white);letter-spacing:1px;display:block}
  .headline .big{font-size:130px;color:var(--red);display:block}
  .headline .room{font-size:90px;color:var(--white);display:block}
  .headline .room span{color:var(--red)}
  .title-rule{position:absolute;left:50px;top:570px;width:300px;height:3px;background:var(--red)}

  .about{position:absolute;left:50px;top:582px;width:410px}
  .about h3{font-size:14px;font-weight:700;margin-bottom:4px}
  .about p{font-size:11px;line-height:1.5;color:var(--text-soft)}

  .benefits{position:absolute;left:50px;top:702px;width:410px}
  .benefits h2{font-family:'Oswald',sans-serif;font-weight:700;font-size:24px;line-height:1.2;color:var(--red);margin-bottom:6px}
  .benefits dt{font-size:12px;font-weight:700;color:var(--red);line-height:1.3}
  .benefits dd{font-size:10.5px;color:var(--text-soft);margin-bottom:4px;line-height:1.35}

  .offer-panel{position:absolute;left:470px;top:330px;width:400px;height:460px;background:var(--red)}
  .coupon{position:absolute;left:500px;top:350px;width:340px;height:270px;background:var(--white);color:var(--ink);text-align:center}
  .coupon::before,.coupon::after{content:"";position:absolute;top:0;width:14px;height:100%;
    background:radial-gradient(circle at center,var(--red) 5px,transparent 5.5px) 0 0/14px 16px repeat-y}
  .coupon::before{left:-7px}
  .coupon::after{right:-7px}
  .coupon-head{background:var(--red);padding:12px 0 8px;color:var(--white)}
  .coupon-head .tag{display:inline-block;border:2px solid var(--white);padding:2px 12px;font-family:'Oswald',sans-serif;font-weight:700;font-size:24px;letter-spacing:.5px}
  .coupon-head .sub{font-size:13px;margin-top:4px}
  .coupon .try{font-family:'Oswald',sans-serif;font-weight:700;font-size:17px;line-height:1.15;margin-top:10px}
  .coupon .price{display:inline-block;background:var(--red);color:var(--white);border-radius:12px;font-family:'Bebas Neue',sans-serif;font-size:78px;line-height:1;padding:4px 26px 0;margin:6px 0 2px}
  .coupon .regular{font-family:'Oswald',sans-serif;font-weight:700;font-size:20px}

  .why{position:absolute;left:492px;top:632px;width:360px}
  .why h2{font-family:'Oswald',sans-serif;font-weight:700;font-size:22px;margin-bottom:4px}
  .why ol{list-style:none;font-size:10.5px;line-height:1.4}
  .why li{margin-bottom:2px}

  .prices{position:absolute;left:470px;top:800px;width:380px;border-collapse:collapse;font-size:12px;text-align:center}
  .prices th,.prices td{padding:4px;height:26px}
  .prices th{font-weight:600}
  .prices .label{border:1px solid var(--white);text-align:left;padding-left:12px;width:130px}
  .prices .member{background:var(--red);width:125px}
  .prices .non{background:var(--yellow);color:var(--ink);width:125px}

  .call{position:absolute;right:20px;top:936px;text-align:right;display:flex;align-items:center;gap:10px}
  .call .lead{font-size:15px;font-weight:600;line-height:1.3}
  .call .num{font-size:22px;font-weight:700;line-height:1.15}
  .call .note{font-size:9px;line-height:1.3}
  .icon-disc{width:34px;height:34px;border-radius:50%;background:var(--red);display:flex;align-items:center;justify-content:center;flex:none}
  .icon-disc.dark{background:var(--ink)}

  .signoff{position:absolute;left:50px;top:958px;font-family:'Bebas Neue',sans-serif;line-height:.95}
  .signoff .name{font-family:'Oswald',sans-serif;font-weight:700;font-size:28px;line-height:1.1;color:var(--white)}
  .signoff .facility{font-size:40px;color:var(--red);display:block}
  .signoff .slogan{font-size:20px;color:var(--white);display:block}

  .web-block{position:absolute;left:500px;top:1000px;width:370px;height:62px;background:var(--red);display:flex;align-items:center;gap:10px;padding-left:22px;font-size:12px;line-height:1.35}
  .footer-band{position:absolute;left:0;top:1062px;width:870px;height:64px;background:var(--red);display:flex;align-items:center;gap:12px;padding-left:50px;font-size:12px;line-height:1.35}
</style>
</head>
<body>
<main class="flyer">
  <div class="hero-photo" role="img" aria-label="Photo of a man relaxing in front of a glowing red light therapy panel"></div>
  <div class="hero-fade"></div>
  <div class="hero-fade-bottom"></div>

  <div class="brand">KorVesta</div>

  <h1 class="headline">
    <span class="intro">Introducing our new</span>
    <span class="big">Red Light</span>
    <span class="big">Therapy</span>
    <span class="room">Room<span>!</span></span>
  </h1>
  <div class="title-rule"></div>

  <section class="about">
    <h3>What is Red Light Therapy?</h3>
    <p>Red Light Therapy (RLT) is a revolutionary treatment that uses specific wavelengths of light to promote healing, reduce inflammation, and enhance overall well-being. At KorVesta, we are excited to offer the advanced Quorvane Glow Therapy TelaRix 700 panels—designed to maximize your health benefits in a relaxing environment.</p>
  </section>

  <section class="benefits">
    <h2>BENEFITS OF RED LIGHT THERAPY:</h2>
    <dl>
      <dt>Boosts Energy Levels:</dt><dd>Feel revitalized and more energetic after each session.</dd>
      <dt>Enhances Muscle Recovery:</dt><dd>Speed up recovery times post workout and reduce soreness.</dd>
      <dt>Improves Skin Health:</dt><dd>Reduce wrinkles, blemishes, and promote a youthful glow.</dd>
      <dt>Supports Joint Health:</dt><dd>Alleviate pain and inflammation, making movement easier.</dd>
      <dt>Promotes Better Sleep:</dt><dd>Improve your sleep patterns and overall restfulness.</dd>
      <dt>Increases Circulation:</dt><dd>Enhance blood flow for better nutrient delivery to muscles.</dd>
    </dl>
  </section>

  <div class="offer-panel"></div>
  <section class="coupon">
    <div class="coupon-head">
      <div class="tag">LIMITED TIME ONLY!</div>
      <div class="sub">Special Introductory Offer!</div>
    </div>
    <div class="try">TRY YOUR FIRST SESSION<br>FOR JUST</div>
    <div class="price">$25</div>
    <div class="regular">REGULARLY $55</div>
  </section>

  <section class="why">
    <h2>WHY CHOOSE KORVESTA?</h2>
    <ol>
      <li>(1) State-of-the-Art Equipment: Experience the power of eight Quorvane Glow Therapy TelaRix 700 panels—some of the best on the market!</li>
      <li>(2) Expert Guidance: Our trained staff will guide you through each session to ensure you get the most out of your therapy.</li>
      <li>(3) Community Focused: Join a supportive community that prioritizes health and wellness.</li>
    </ol>
  </section>

  <table class="prices">
    <tr><th class="label">PRICES</th><th class="member">KorVesta Member</th><th class="non">Non-Member</th></tr>
    <tr><td class="label">SINGLE SESSION</td><td class="member">$35</td><td class="non">$55</td></tr>
    <tr><td class="label">3 – PACK</td><td class="member">$102</td><td class="non">$159</td></tr>
    <tr><td class="label">5 – PACK</td><td class="member">$167</td><td class="non">$259</td></tr>
    <tr><td class="label">10 – PACK</td><td class="member">$316</td><td class="non">$491</td></tr>
  </table>

  <div class="call">
    <div>
      <div class="lead">Call Us at</div>
      <div class="num">(555) 204-3187</div>
      <div class="note">to schedule your appointment.</div>
    </div>
    <div class="icon-disc">
      <svg width="18" height="18" viewBox="0 0 24 24" fill="#fff"><path d="M6.6 10.8a15.1 15.1 0 0 0 6.6 6.6l2.2-2.2a1 1 0 0 1 1-.25 11.4 11.4 0 0 0 3.6.57 1 1 0 0 1 1 1V20a1 1 0 0 1-1 1A17 17 0 0 1 3 4a1 1 0 0 1 1-1h3.5a1 1 0 0 1 1 1c0 1.250.2 2.450.57 3.6a1 1 0 0 1-.25 1z"/></svg>
    </div>
  </div>

  <div class="signoff">
    <div class="name">KorVesta</div>
    <span class="facility">Fitness Facility</span>
    <span class="slogan">Your wellness, our commitment!</span>
  </div>

  <div class="web-block">
    <div class="icon-disc dark">
      <svg width="18" height="18" viewBox="0 0 24 24" fill="none" stroke="#fff" stroke-width="1.8"><circle cx="12" cy="12" r="9"/><path d="M3 12h18M12 3c3 3.2 3 14.8 0 18M12 3c-3 3.2-3 14.8 0 18"/></svg>
    </div>
    <div>yoursite goes here.com<br>yoursite goes here.com</div>
  </div>

  <footer class="footer-band">
    <div class="icon-disc dark">
      <svg width="16" height="18" viewBox="0 0 24 24" fill="#fff"><path d="M12 2a7 7 0 0 0-7 7c0 5 7 13 7 13s7-8 7-13a7 7 0 0 0-7-7zm0 9.5A2.5 2.5 0 1 1 12 6.5a2.5 2.5 0 0 1 0 5z"/></svg>
    </div>
    <div>Street Address Here<br>lorem, 0000</div>
  </footer>
</main>
</body>
</html>
```